www.copperleaf-nimbo.com web Page

Discover Quito Discover Otavalo Discover Cotopaxi Discover Discover Discover Mindo Birdwatching Discover Quilotoa Discover Amazonas Discover Galapagos Islands
Updates

Thank you all sending proyect designs..If you have not received a reply from us than your design has not met our original requirements .... Best Regards, Ruben

Target Market(s)

USA / Europe England,

Number of Pages Required

5+ page

Font styles to use
Sans Serif

Requirements
Must have
• I will need Logo to be upgraded instead of 17 years, it need to say 25 years. Userfriendly design, SEO friendly and responsive. Web needs to work on all devices like Android, IOS, Tablet and Windows
Nice to have
• Please consider 1. Minimalistic design 2. Copperleaf Nimbo logo in feautred areas fo web pages 3. Modular design 4. Hero not sliding images 5. Landing page with full with image 6. Elements with animations 7. Hamburger menu 8. I will drop the Packages part of www.copperleaf-nimbo.com 9. Incorporate Galapagos Islands instead 10. I will concentrate on the modular design to have Discover Quito Discover Otavalo Discover Cotopaxi Discover Discover Discover Mindo Birdwatching Discover Quilotoa Discover Amazonas Discover Galapagos Islands
Should not have
• Sliding images

```html
<!DOCTYPE html>
<html lang="en">
<head>
<meta charset="utf-8">
<title>Copperleaf Nimbo – Ecuador Tours</title>
<link href="https://fonts.googleapis.com/css2?family=Oswald:wght@500;700&family=Roboto:wght@400;500;700&display=swap" rel="stylesheet">
<style>
:root{
  --green:#1ea33c;
  --green-dark:#15882f;
  --blue:#0b62b5;
  --blue-dark:#064a95;
  --blue-light:#2b8fe0;
  --ink:#333a40;
  --muted:#8a9096;
  --line:#d9dde1;
  --paper:#ffffff;
  --mist:#f3f5f7;
}
*{box-sizing:border-box;margin:0;padding:0}
html,body{width:1200px;height:3571px;overflow:hidden;background:var(--paper)}
body{font-family:"Roboto",Arial,sans-serif;color:var(--ink)}
.page{position:relative;width:1200px;height:3571px;overflow:hidden;background:var(--paper)}
.abs{position:absolute}
.heading{font-family:"Oswald","Arial Narrow",sans-serif;font-weight:700;font-style:italic;text-transform:uppercase;text-align:center;letter-spacing:.5px}
.heading .g{color:var(--green)}
.heading .b{color:var(--blue)}
.photo{position:absolute;overflow:hidden}
.btn{position:absolute;background:var(--blue);color:#fff;font-family:"Oswald",sans-serif;font-weight:500;font-size:11px;text-transform:uppercase;display:flex;align-items:center;justify-content:center;letter-spacing:.6px;transform:skewX(-10deg);box-shadow:0 3px 6px rgba(0,0,0,.2)}
.btn span{transform:skewX(10deg)}
.lorem{font-size:11px;line-height:19px;color:var(--muted);text-align:center}

/* header */
.brand{left:210px;top:16px;width:150px;height:76px;display:flex;align-items:center;gap:8px}
.brand-mark{width:22px;height:22px;background:var(--green);border-radius:50%}
.brand-name{font-family:"Roboto",sans-serif;font-weight:700;font-size:16px;color:var(--blue-dark);line-height:18px}
.contact-top{top:30px;display:flex;align-items:center;gap:8px;font-size:10px;color:#fff}
.contact-top b{display:block;font-size:13px}
.phone-dot{width:24px;height:24px;border-radius:50%;background:var(--blue);display:flex;align-items:center;justify-content:center}
.burger{left:966px;top:38px;width:22px}
.burger i{display:block;height:3px;background:var(--blue-dark);margin-bottom:4px;border-radius:2px}

/* search */
.search{top:640px;left:210px;width:790px;height:66px}
.field label{display:block;font-family:"Oswald",sans-serif;font-size:11px;font-weight:500;color:var(--blue-dark);text-transform:uppercase;margin-bottom:8px}
.field div{height:28px;border:1px solid var(--line);font-size:10px;color:var(--muted);padding:8px}

/* tours */
.tour-card{position:absolute;top:1155px;height:195px;border:3px solid #fff;box-shadow:0 8px 16px rgba(0,0,0,.3);overflow:hidden}
.tour-card .cap{position:absolute;bottom:12px;width:100%;text-align:center;color:#fff;font-family:"Oswald",sans-serif;font-weight:500;font-size:12px;text-transform:uppercase}
.tour-feature{background:linear-gradient(160deg,#2a86d6,#0c4c92);color:#fff;padding:40px 16px;text-align:center}
.tour-feature h4{font-family:"Oswald",sans-serif;font-size:12px;text-transform:uppercase;margin-bottom:8px}
.tour-feature p{font-size:9px;line-height:13px}

/* lodges */
.lodge{position:absolute;top:1481px;width:243px;height:293px;background:#fff;box-shadow:0 6px 18px rgba(0,0,0,.12)}
.lodge .photo{left:0;top:0;width:243px;height:190px}
.lodge h5{position:absolute;top:204px;width:100%;text-align:center;font-family:"Oswald",sans-serif;font-weight:700;font-size:13px;color:var(--green);text-transform:uppercase}
.lodge p{position:absolute;top:228px;left:24px;right:24px;font-size:9.5px;line-height:14px;color:var(--muted);text-align:center}
.arrow{position:absolute;width:26px;height:26px;border-radius:50%;background:var(--blue);display:flex;align-items:center;justify-content:center}

/* destinations */
.dest-label{position:absolute;font-family:"Oswald",sans-serif;font-weight:700;font-style:italic;font-size:13px;color:var(--green);text-transform:uppercase}
.dest{box-shadow:0 6px 14px rgba(0,0,0,.2)}

/* review */
.review{position:absolute;top:2738px;width:340px;height:83px}
.review .avatar{position:absolute;left:0;top:5px;width:72px;height:72px;border:3px solid #fff;background:#c9a58a;box-shadow:0 3px 8px rgba(0,0,0,.3)}
.review .bubble{position:absolute;left:80px;top:0;width:260px;height:83px;background:#fff;border-radius:4px;padding:12px 14px;font-size:9px;line-height:14px;color:var(--muted)}
.review .who{margin-top:12px;font-family:"Oswald",sans-serif;font-size:10px;color:var(--blue);text-transform:uppercase}
.review .who em{color:var(--green);font-style:normal;margin-left:10px;letter-spacing:1px}
.review .q{position:absolute;right:18px;bottom:8px;font-family:"Oswald",sans-serif;font-size:40px;color:#dfe3e6;line-height:30px}

/* partners */
.partner{position:absolute;top:3107px;width:174px;height:72px;background:#fff;box-shadow:0 4px 12px rgba(0,0,0,.12);display:flex;align-items:center;justify-content:center}
.partner i{display:block;background:#d3d7db}

/* footer */
.footer{left:0;top:3240px;width:1200px;height:295px;background:var(--green)}
.fcol{position:absolute;top:58px;color:#fff}
.fcol h6{font-family:"Oswald",sans-serif;font-weight:700;font-style:italic;font-size:17px;text-transform:uppercase;margin-bottom:14px}
.fcol li{list-style:none;font-size:10px;text-transform:uppercase;margin-bottom:12px}
.fcol .faq li{text-transform:none;margin-bottom:8px}
.crow{display:flex;gap:8px;align-items:flex-start;font-size:10px;margin-bottom:10px}
.crow .ic{width:20px;height:20px;background:#fff;border-radius:3px;flex:none}
.crow b{font-size:14px}
.badge{position:absolute;background:#fff;border-radius:2px}
.copy{left:0;top:3535px;width:1200px;height:36px;background:var(--blue-dark);color:#fff;font-size:10px;display:flex;align-items:center;padding:0 210px;justify-content:space-between}
.copy .follow{font-family:"Oswald",sans-serif;font-size:13px;display:flex;align-items:center;gap:10px}
.copy .follow i{width:22px;height:22px;background:var(--blue-light);display:block}
</style>
</head>
<body>
<div class="page">

  <!-- HERO -->
  <div class="photo" style="left:0;top:0;width:1200px;height:585px;background:linear-gradient(180deg,#b9d4ea 0%,#8fb6cf 35%,#5f8a5a 65%,#3f6e36 100%)" role="img" aria-label="Traveller holding an open map overlooking green Andean mountains"></div>
  <svg class="abs" style="left:0;top:500px" width="1200" height="100" viewBox="0 0 1200 100" aria-hidden="true">
    <path d="M0 70 L40 58 L70 72 L110 50 L150 66 L190 55 L230 74 L270 60 L310 70 L350 52 L390 68 L430 58 L470 76 L520 62 L560 72 L600 56 L640 70 L680 60 L720 74 L760 58 L800 68 L840 52 L880 66 L920 60 L960 72 L1000 56 L1040 66 L1080 58 L1120 70 L1160 60 L1200 68 L1200 100 L0 100Z" fill="#fff"/>
  </svg>

  <!-- HEADER -->
  <div class="abs" style="left:0;top:0;width:1200px;height:100px;background:rgba(255,255,255,.55)"></div>
  <div class="abs brand"><span class="brand-mark"></span><span class="brand-name">Copperleaf<br>Nimbo</span></div>
  <div class="abs contact-top" style="left:652px">
    <span class="phone-dot"><svg width="12" height="12" viewBox="0 0 24 24"><path d="M6.6 10.8a15 15 0 006.6 6.6l2.2-2.2a1 1 0 011-.25 11 11 0 003.6.6 1 1 0 011 1V20a1 1 0 01-1 1A17 17 0 013 4a1 1 0 011-1h3.5a1 1 0 011 1 11 11 0 00.6 3.6 1 1 0 01-.25 1z" fill="#fff"/></svg></span>
    <div style="color:var(--blue-dark)">24 Hours Phone<b>(555+2) 410 7731</b></div>
  </div>
  <div class="abs contact-top" style="left:812px">
    <span class="phone-dot"><svg width="12" height="12" viewBox="0 0 24 24"><path d="M6.6 10.8a15 15 0 006.6 6.6l2.2-2.2a1 1 0 011-.25 11 11 0 003.6.6 1 1 0 011 1V20a1 1 0 01-1 1A17 17 0 013 4a1 1 0 011-1h3.5a1 1 0 011 1 11 11 0 00.6 3.6 1 1 0 01-.25 1z" fill="#fff"/></svg></span>
    <div style="color:var(--blue-dark)">Phone / Fax<b>(555+2) 410 7732</b></div>
  </div>
  <div class="abs burger"><i></i><i></i><i></i></div>

  <!-- SEARCH -->
  <div class="abs search">
    <div class="abs field" style="left:0;width:210px"><label>Where to go ?</label><div>enter country</div></div>
    <div class="abs field" style="left:295px;width:190px"><label>Start date</label><div>dd/mm/yyyy</div></div>
    <div class="abs field" style="left:495px;width:190px"><label>Person</label><div>0</div></div>
    <div class="abs" style="left:695px;top:24px;width:90px;height:28px;background:var(--blue);color:#fff;font-size:10px;display:flex;align-items:center;justify-content:center;gap:12px">Find now
      <svg width="11" height="11" viewBox="0 0 24 24"><circle cx="10" cy="10" r="7" stroke="#fff" stroke-width="3" fill="none"/><path d="M15 15l6 6" stroke="#fff" stroke-width="3"/></svg></div>
  </div>

  <!-- ABOUT -->
  <h2 class="abs heading" style="left:0;top:735px;width:1200px;font-size:30px"><span class="g">About Us</span></h2>
  <p class="abs lorem" style="left:210px;top:797px;width:780px">Lorem ipsum dolor sit amet, consectetur adipiscing elit. Aliquam gravida quis augue a molestie. Duis pharetra felis nulla. Ut nibh erat, commodo a felis ut, dignissim tempus purus. In tincidunt eleifend elit, quis faucibus neque convallis eget. Phasellus non tincidunt justo, sed convallis erat. Proin vitae justo nec nibh facilisis aliquam ut sed ante. Vivamus vitae libero a felis cursus rhoncus vitae at tellus. Suspendisse potenti. Quisque malesuada orci felis sed ultrices. Curabitur tristique iaculis eleifend. Sed nisl nulla tristique, convallis ex a, volutpat erat. Vivamus iaculis velit non eleifend laoreet.</p>
  <div class="btn" style="left:556px;top:928px;width:90px;height:26px"><span>Read more</span></div>

  <!-- OUR TOURS -->
  <svg class="abs" style="left:0;top:1015px" width="1200" height="430" viewBox="0 0 1200 430" aria-hidden="true">
    <defs><linearGradient id="tourBand" x1="0" y1="0" x2="0" y2="1"><stop offset="0" stop-color="#1f7fd4"/><stop offset="1" stop-color="#0a56a8"/></linearGradient></defs>
    <path d="M0 30 L30 18 L60 28 L100 10 L140 24 L180 8 L220 22 L260 12 L300 26 L340 6 L380 20 L420 10 L460 24 L500 8 L540 22 L580 12 L620 26 L660 6 L700 20 L740 10 L780 24 L820 8 L860 20 L900 10 L940 26 L980 8 L1020 22 L1060 12 L1100 26 L1140 10 L1200 22 L1200 405 Q1180 385 1150 405 Q1120 385 1090 405 Q1060 385 1030 405 Q1000 385 970 405 Q940 385 910 405 Q880 385 850 405 Q820 385 790 405 Q760 385 730 405 Q700 385 670 405 Q640 385 610 405 Q580 385 550 405 Q520 385 490 405 Q460 385 430 405 Q400 385 370 405 Q340 385 310 405 Q280 385 250 405 Q220 385 190 405 Q160 385 130 405 Q100 385 70 405 Q40 385 0 405Z" fill="url(#tourBand)"/>
  </svg>
  <h2 class="abs heading" style="left:0;top:1058px;width:1200px;font-size:30px;color:#fff">Our Tours</h2>

  <div class="tour-card tour-feature" style="left:210px;width:176px;transform:rotate(-2deg)">
    <h4>Birdwatching Tours</h4>
    <p>Our guest house was built with the idea for you to enjoy one of the most</p>
    <div class="btn" style="left:54px;top:122px;width:64px;height:20px;font-size:9px;background:#0b2d5c"><span>Book now</span></div>
  </div>
  <div class="tour-card" style="left:405px;width:181px">
    <div class="photo" style="inset:0;background:linear-gradient(160deg,#9cc6e8,#e7c9a6 60%,#b58a62)" role="img" aria-label="Group of friends with balloons on a day tour"></div>
    <div class="cap">Day Tours</div>
  </div>
  <div class="tour-card" style="left:610px;width:178px">
    <div class="photo" style="inset:0;background:linear-gradient(170deg,#7fa65f,#3f6b35 60%,#2b4a27)" role="img" aria-label="Traveller on a zip line above the Mindo forest"></div>
    <div class="cap">Mindo Day Tours</div>
  </div>
  <div class="tour-card" style="left:812px;width:176px">
    <div class="photo" style="inset:0;background:linear-gradient(170deg,#8a9a6d,#5e6e45 55%,#3d4a2e)" role="img" aria-label="Visitors on a canoe trip through the Amazon"></div>
    <div class="cap">Amazon Lodges &amp; Tours</div>
  </div>

  <!-- LODGES -->
  <div class="abs" style="left:0;top:1430px;width:1200px;height:380px;background:linear-gradient(180deg,#f4f6f8,#ffffff)"></div>
  <div class="arrow" style="left:154px;top:1615px"><svg width="10" height="10" viewBox="0 0 10 10"><path d="M7 1L3 5l4 4" stroke="#fff" stroke-width="2" fill="none"/></svg></div>
  <div class="arrow" style="left:1020px;top:1615px"><svg width="10" height="10" viewBox="0 0 10 10"><path d="M3 1l4 4-4 4" stroke="#fff" stroke-width="2" fill="none"/></svg></div>

  <div class="lodge" style="left:214px">
    <div class="photo" style="background:linear-gradient(170deg,#b9c7d2,#b35b5b 55%,#6f4a3e)" role="img" aria-label="Guest house patio with wicker chairs and red cushions"></div>
    <h5>Quito Guest House</h5>
    <p>Our guest house was built with the ideal for you to enjoy one of the most</p>
    <div class="btn" style="left:82px;top:268px;width:78px;height:20px;font-size:9px"><span>View site</span></div>
  </div>
  <div class="lodge" style="left:481px">
    <div class="photo" style="background:linear-gradient(170deg,#4f7a3d,#2f5a2a 60%,#5a4a3a)" role="img" aria-label="Group of visitors in the cloud forest garden"></div>
    <h5>Tulipe Pachijal Cloud Forest</h5>
    <p>Our guest house was built with the ideal for you to enjoy one of the most</p>
    <div class="btn" style="left:82px;top:268px;width:78px;height:20px;font-size:9px"><span>View site</span></div>
  </div>
  <div class="lodge" style="left:748px">
    <div class="photo" style="background:linear-gradient(170deg,#4fa6c8,#1f6f96 55%,#0e4763)" role="img" aria-label="Sea lion swimming underwater near the islands"></div>
    <h5>Galapagos Cruises and Tours</h5>
    <p>Our guest house was built with the ideal for you to enjoy one of the most</p>
    <div class="btn" style="left:82px;top:268px;width:78px;height:20px;font-size:9px"><span>Visit site</span></div>
  </div>

  <!-- CHOOSE DESTINATION -->
  <h2 class="abs heading" style="left:0;top:1873px;width:1200px;font-size:30px"><span class="g">Choose</span> <span class="b">Destination</span></h2>
  <p class="abs lorem" style="left:210px;top:1930px;width:780px">Lorem ipsum dolor sit amet, consectetur adipiscing elit. Aliquam gravida quis augue a molestie. Duis pharetra felis nulla. Ut nibh erat, commodo a felis ut, dignissim tempus purus. In tincidunt eleifend elit, quis faucibus neque convallis eget.</p>

  <div class="dest-label" style="left:83px;top:1958px">Discover Quito</div>
  <div class="photo dest" style="left:43px;top:2055px;width:188px;height:247px;background:linear-gradient(170deg,#2a5fb8,#3c72c4 55%,#6b7a8a)" role="img" aria-label="Winged virgin statue on El Panecillo against blue sky"></div>

  <div class="abs dest" style="left:290px;top:2000px;width:360px;height:281px;background:linear-gradient(160deg,#3fbf5a,#1c9a3a)" role="img" aria-label="Green forest foliage behind the Mindo birdwatching panel"></div>
  <div class="abs" style="left:290px;top:2125px;width:360px;text-align:center;color:#fff">
    <div style="font-family:'Oswald',sans-serif;font-weight:500;font-size:16px">Discover Mindo Birdwatching</div>
    <div style="font-size:9px;margin-top:8px;opacity:.85">Lorem ipsum dolor sit amet, consectetur adipiscing elit</div>
    <div style="margin:16px auto 0;width:26px;height:26px;border-radius:50%;background:var(--blue);display:flex;align-items:center;justify-content:center"><svg width="10" height="10" viewBox="0 0 10 10"><path d="M3 1l4 4-4 4" stroke="#fff" stroke-width="2" fill="none"/></svg></div>
  </div>

  <div class="dest-label" style="left:731px;top:2080px">Discover Galapagos Islands</div>
  <div class="photo dest" style="left:710px;top:2114px;width:252px;height:298px;background:linear-gradient(180deg,#8ec3e6 0%,#c9e3f2 40%,#4fb0c6 60%,#e3d6b8 80%,#cbb994)" role="img" aria-label="Sea lions resting on a white sand beach"></div>
  <div class="btn" style="left:745px;top:2445px;width:184px;height:36px;font-size:13px"><span>View all destination</span></div>

  <div class="dest-label" style="left:1036px;top:1997px">Discover Amazonas</div>
  <div class="photo dest" style="left:1019px;top:2029px;width:176px;height:250px;background:linear-gradient(170deg,#8fc3e8,#3f7d3c 45%,#2a5e30 70%,#4a7fa0)" role="img" aria-label="Aerial view of the Amazon river through rainforest"></div>

  <div class="dest-label" style="left:19px;top:2347px">Discover Otavalo</div>
  <div class="photo dest" style="left:0;top:2381px;width:169px;height:179px;background:linear-gradient(170deg,#7ea9d6,#b9a38a 50%,#8a6a4e)" role="img" aria-label="Otavalo town square and cathedral"></div>

  <div class="photo dest" style="left:229px;top:2333px;width:188px;height:167px;background:linear-gradient(180deg,#3b78c6 0%,#e9eef2 45%,#6d8a5a 75%,#4f6b3e)" role="img" aria-label="Snow capped Cotopaxi volcano"></div>
  <div class="dest-label" style="left:250px;top:2514px">Discover Cotopaxi</div>

  <div class="dest-label" style="left:495px;top:2357px">Discover Quilotoa</div>
  <div class="photo dest" style="left:462px;top:2393px;width:202px;height:167px;background:linear-gradient(180deg,#a8cbe6,#7f8f6a 40%,#2f8a86 65%,#1f6f70)" role="img" aria-label="Turquoise Quilotoa crater lake"></div>

  <div class="photo dest" style="left:1000px;top:2314px;width:181px;height:186px;background:linear-gradient(170deg,#4f8a3c,#2e5e2a 60%,#6a5a3a)" role="img" aria-label="Adventurer swinging above the Baños jungle"></div>
  <div class="dest-label" style="left:1033px;top:2509px">Discover Baños</div>

  <!-- TOURIST REVIEW -->
  <svg class="abs" style="left:0;top:2595px" width="1200" height="310" viewBox="0 0 1200 310" aria-hidden="true">
    <defs><linearGradient id="revBand" x1="0" y1="0" x2="1" y2="0"><stop offset="0" stop-color="#0a4e9c"/><stop offset=".5" stop-color="#1a7fd2"/><stop offset="1" stop-color="#0a4e9c"/></linearGradient></defs>
    <path d="M0 18 L60 8 L120 20 L180 6 L240 18 L300 10 L360 22 L420 6 L480 18 L540 8 L600 20 L660 6 L720 18 L780 10 L840 22 L900 6 L960 18 L1020 8 L1080 20 L1140 8 L1200 18 L1200 285 L1140 298 L1080 284 L1020 296 L960 286 L900 300 L840 286 L780 296 L720 284 L660 298 L600 286 L540 296 L480 284 L420 298 L360 286 L300 296 L240 284 L180 298 L120 286 L60 296 L0 286Z" fill="url(#revBand)"/>
  </svg>
  <h2 class="abs heading" style="left:0;top:2647px;width:1200px;font-size:30px;color:#fff">Tourist Review</h2>

  <div class="review" style="left:231px">
    <div class="avatar" role="img" aria-label="Reviewer portrait"></div>
    <div class="bubble">Curabitur vel lacus non. Proin pretium et scelerisque semper aliquam interdum.
      <div class="who">Alden Marsh <em>★★★★★</em></div>
      <div class="q">”</div>
    </div>
  </div>
  <div class="review" style="left:626px">
    <div class="avatar" role="img" aria-label="Reviewer portrait" style="background:#b99478"></div>
    <div class="bubble">Curabitur vel lacus non. Proin pretium et scelerisque semper aliquam interdum.
      <div class="who">Colin Varga <em>★★★★★</em></div>
      <div class="q">”</div>
    </div>
  </div>

  <!-- NEWSLETTER -->
  <h2 class="abs heading" style="left:0;top:2922px;width:1200px;font-size:22px"><span class="b">Subcribe to the Newsletter</span></h2>
  <div class="abs" style="left:345px;top:2980px;width:370px;height:40px;border:1px solid var(--line);border-radius:20px 0 0 20px;font-size:10px;color:var(--muted);padding:13px 20px">Enter Your Email ......</div>
  <div class="abs" style="left:713px;top:2980px;width:137px;height:40px;background:linear-gradient(90deg,var(--blue-dark),var(--blue-light));border-radius:0 20px 20px 0;color:#fff;font-family:'Oswald',sans-serif;font-size:13px;display:flex;align-items:center;justify-content:center;gap:8px">
    <svg width="12" height="12" viewBox="0 0 24 24"><path d="M2 12L22 3l-6 19-4-8z" fill="#fff"/></svg>Subcribe Now</div>

  <!-- PARTNERS -->
  <div class="arrow" style="left:154px;top:3130px"><svg width="10" height="10" viewBox="0 0 10 10"><path d="M7 1L3 5l4 4" stroke="#fff" stroke-width="2" fill="none"/></svg></div>
  <div class="arrow" style="left:1020px;top:3130px"><svg width="10" height="10" viewBox="0 0 10 10"><path d="M3 1l4 4-4 4" stroke="#fff" stroke-width="2" fill="none"/></svg></div>
  <div class="partner" style="left:214px"><i style="width:34px;height:40px"></i></div>
  <div class="partner" style="left:410px"><i style="width:100px;height:28px"></i></div>
  <div class="partner" style="left:614px"><i style="width:104px;height:24px"></i></div>
  <div class="partner" style="left:821px"><i style="width:60px;height:36px;border-radius:50%"></i></div>

  <!-- FOOTER -->
  <svg class="abs" style="left:0;top:3205px" width="1200" height="40" viewBox="0 0 1200 40" aria-hidden="true">
    <path d="M0 40 Q30 10 60 28 Q90 8 120 26 Q150 6 180 24 Q210 8 240 28 Q270 10 300 26 Q330 6 360 24 Q390 10 420 28 Q450 8 480 26 Q510 6 540 24 Q570 10 600 28 Q630 8 660 26 Q690 6 720 24 Q750 10 780 28 Q810 8 840 26 Q870 6 900 24 Q930 10 960 28 Q990 8 1020 26 Q1050 6 1080 24 Q1110 10 1140 28 Q1170 8 1200 26 L1200 40Z" fill="var(--green)"/>
  </svg>
  <div class="abs footer">
    <div class="fcol" style="left:210px">
      <h6>Quick Links</h6>
      <ul><li>Home</li><li>About Us</li><li>Our Tours</li><li>Destination</li><li>Reviews</li><li>Contact Us</li></ul>
    </div>
    <div class="fcol" style="left:376px;width:200px">
      <h6>Contact Us</h6>
      <div class="crow"><span class="ic"></span><span><b style="font-size:11px">COPPERLEAF NIMBO</b><br>CALLE FERRO ALTO<br>N3-22 Y LUMEN, QUITO</span></div>
      <div class="crow" style="align-items:center"><span class="ic"></span><b>555-2-410-7731</b></div>
      <div class="crow" style="align-items:center"><span class="ic"></span><b>555-2-410-7732</b></div>
      <div class="crow" style="align-items:center"><span class="ic"></span>info@copperleaf-nimbo.com</div>
    </div>
    <div class="fcol" style="left:595px;width:150px">
      <h6>Ecuador FAQ</h6>
      <ul class="faq"><li>About Ecuador</li><li>Tips for the Tourist</li><li>10 Reasons for travelling to Ecuador</li><li>Experiences</li><li>Moments</li><li>Connectivity</li></ul>
    </div>
    <div class="fcol" style="left:757px;font-size:10px;font-family:'Oswald',sans-serif;font-style:italic;font-weight:700">MEMBER OF</div>
    <div class="badge" style="left:757px;top:76px;width:126px;height:50px"></div>
    <div class="fcol" style="left:900px;font-size:10px;font-family:'Oswald',sans-serif;font-style:italic;font-weight:700">AWARD</div>
    <div class="badge" style="left:900px;top:76px;width:88px;height:50px"></div>
    <div class="fcol" style="left:757px;top:140px;font-size:10px;font-family:'Oswald',sans-serif;font-style:italic;font-weight:700">ECUADOR BRAND</div>
    <div class="badge" style="left:757px;top:158px;width:58px;height:54px"></div>
    <div class="badge" style="left:826px;top:158px;width:54px;height:54px;border-radius:50%"></div>
    <div class="abs" style="left:900px;top:160px;width:88px;height:50px;display:flex;align-items:center;justify-content:center;color:#fff;font-weight:700;font-size:11px;text-align:center;line-height:13px">Copperleaf<br>Nimbo</div>
  </div>
  <div class="abs" style="left:1190px;top:3318px;width:8px;height:8px;border-radius:50%;background:#fff"></div>
  <div class="abs copy">
    <span>© COPYRIGHT 2018 COPPERLEAF NIMBO. ALL RIGHTS RESERVED</span>
    <span class="follow">FOLLOW US <i></i></span>
  </div>

</div>
</body>
</html>
```